Performance Coaching business needs brochure design

I need a brochure designed that will be given to attendants at an IT / Accountancy conference.
Aim: The brochure is to encourage people to take up the offer that will be on there.
My business: KV Stride Mentoring. I coach people in corporate jobs how to improve performance through keeping fitn and healthy.
The brochure: I will post a list of notes (2 pages) I have and the winning designer is to use these notes to take out the most important points and create a powerful, enticing brochure that meets the following guidlines:
Why staff health is important to business? You will quote stats and reasons why it is important.
What staff want from their employer?
What I do?
Case study
Enticing Offer
The winning design will use powerful images, and will be light on words. The words used will answer the above points (these points dont't necessarily need to be on the brochure in the wording I have used here).
You can use my website www.kvstridementoring.example for ideas.
Updates
Apologies but I have been advised of a slight change. I now require A4 size design. It needs to go into a folder with a lot of other information. My new requirements are:
a) 2-3 pages max. either 1 front and back and an offer page, or 2 -3 single sided pages. whatever looks best
b) page or section 1 must be about why personal health/wellbeing is important to business. Include stats from my handouts as well as reasons why
c) section 2 is about what benefit health is to staff (eg....they get more from their company, they are better at their job, their performance is enhanced etc
d) page or section 3 must include about me (from my website www.kvstridementoring.example) and results from LMD
d) section 4 is the offer to LMD delegates.
FYI LMD (company holding the conference) website is www.lmd-forward.example use it for their logo if you need
This format has been confirmed and aplogies for the change
Target Market(s)
Accountancy firms.
Industry/Entity Type
Health
Requirements
Must have
- Can be either a fold up style brochure or a flyer with front & back. Must be easy to print as I will need to print it as soon as possible.
The images supplied are just a guide...use if you like
Nice to have
- I'd like to see a design the portrays success, change, health, simplicity, clarity.

```html
<!DOCTYPE html>
<html lang="en">
<head>
<meta charset="utf-8">
<title>KV Stride Mentoring – Brochure</title>
<link rel="stylesheet" href="https://fonts.googleapis.com/css2?family=Montserrat:wght@700&family=Arimo:ital,wght@0,400;0,700;1,400&display=swap">
<style>
  :root {
    --ink: #3a3a3c;
    --panel: #4b4b4e;
    --panel-deep: #414144;
    --accent: #f1e400;
    --paper: #ffffff;
    --backdrop: #e9e9ea;
    --text-light: #f2f2f2;
    --text-muted: #cfcfd2;
  }
  * { box-sizing: border-box; margin: 0; padding: 0; }
  html, body { width: 1200px; height: 900px; overflow: hidden; }
  body {
    background: var(--backdrop);
    font-family: "Arimo", Arial, sans-serif;
    position: relative;
  }
  .page {
    position: absolute;
    top: 47px;
    width: 570px;
    height: 806px;
    background: var(--panel);
    box-shadow: 0 3px 14px rgba(0,0,0,.22);
    overflow: hidden;
    color: var(--text-light);
    font-size: 9px;
    line-height: 1.35;
  }
  .page--left { left: 20px; }
  .page--right { left: 610px; }

  .masthead {
    background: var(--paper);
    height: 150px;
    padding: 26px 34px 0;
    position: relative;
  }
  .masthead::after {
    content: "";
    position: absolute;
    left: 0; right: 0; bottom: 0;
    height: 6px;
    background: var(--accent);
  }
  .brand-name {
    font-family: "Montserrat", Arial, sans-serif;
    font-weight: 700;
    color: var(--ink);
    font-size: 46px;
    line-height: 1;
    letter-spacing: -1px;
  }
  .brand-name span { display: block; font-size: 34px; margin-top: 6px; letter-spacing: 0; }

  .content { padding: 18px 34px 0; }
  .quote {
    text-align: center;
    font-style: italic;
    font-size: 12px;
    line-height: 1.35;
    margin: 6px 30px 16px;
  }
  .quote em { color: var(--accent); display: block; }
  .quote cite { display: block; font-style: normal; font-size: 13px; text-align: right; margin-top: 2px; }

  .section-title {
    color: var(--accent);
    font-weight: 700;
    font-size: 11.5px;
    margin: 12px 0 4px;
  }
  p { margin-bottom: 4px; }
  strong { font-weight: 700; }
  ul { list-style: none; margin: 3px 0 4px; }
  li { padding-left: 9px; position: relative; }
  li::before { content: "•"; position: absolute; left: 0; color: var(--text-light); }

  .two-col { display: flex; gap: 26px; margin-top: 10px; }
  .two-col > div { flex: 1; }

  .split { display: flex; gap: 16px; align-items: flex-start; }
  .split__text { flex: 1; }
  .image-slot { flex: none; border: 2px solid var(--paper); }
  .slot-handshake {
    width: 186px; height: 126px; margin-top: 10px;
    background: linear-gradient(135deg, #f6f6f6 0%, #dcdcdc 60%, #bdbdbd 100%);
  }
  .slot-portrait {
    width: 160px; height: 118px;
    background: linear-gradient(180deg, #8fb8d9 0%, #c9d6df 55%, #6d6a66 100%);
  }
  .slot-chart {
    position: absolute; left: 0; bottom: 26px;
    width: 300px; height: 248px;
    border: none;
    background: linear-gradient(160deg, #5b6572 0%, #2f3640 55%, #c9ced6 100%);
  }
  .partner-badge {
    width: 104px; height: 50px; margin-top: 4px;
    background: var(--paper);
    display: flex; align-items: center; justify-content: center;
    color: var(--ink);
    font-weight: 700;
    font-size: 14px;
  }
  .highlight { color: var(--accent); }

  .offer-aside {
    position: absolute; left: 320px; bottom: 70px; width: 218px;
  }
  .link { color: var(--accent); font-weight: 700; word-break: break-all; }

  .foot-rule {
    position: absolute; left: 0; right: 0; bottom: 0; height: 6px; background: var(--accent);
  }
  .footer-bar {
    position: absolute; left: 0; right: 0; bottom: 0; height: 26px;
    background: var(--accent);
    color: var(--ink);
    display: flex; justify-content: space-between; align-items: center;
    padding: 0 34px;
    font-size: 10px; font-weight: 700;
  }
</style>
</head>
<body>

<section class="page page--left">
  <header class="masthead">
    <div class="brand-name">KV Stride<span>Mentoring</span></div>
  </header>
  <div class="content">
    <blockquote class="quote">
      “CEOs for decades have been repeating a false story by stating:
      <em>The workers physical body is not business relevant”</em>
      <cite>Jon Lauder</cite>
    </blockquote>

    <h2 class="section-title">Why is health important to business?</h2>
    <p>Health is the missing cog. We have business coaching and more recently EQ (emotional) coaching. For staff to function at their optimum, they must be healthy and have reasonable energy. To think otherwise is false. <strong>Health coaching can provide the missing link to your staffs performance.</strong></p>

    <h2 class="section-title">How can health make a difference?</h2>
    <p>Studies show over a 12 year period, companies with high-performance cultures outperformed their more average peers by:</p>
    <ul>
      <li><strong>4x</strong> revenue growth</li>
      <li><strong>8x</strong> employment growth</li>
    </ul>

    <div class="two-col">
      <div>
        <p>If your staff are fit &amp; healthy you can expect:</p>
        <ul>
          <li>Greater <strong>value</strong> to the business and it’s people</li>
          <li>Increased <strong>profits</strong> and <strong>ROI</strong></li>
          <li>Increased <strong>brand recognition</strong></li>
        </ul>
      </div>
      <div>
        <p>Signs of an unhealthy workforce:</p>
        <ul>
          <li><strong>Disengagement:</strong> Everyone wants to be somewhere else</li>
          <li><strong>1 in 4</strong> employees is overworked and vacations not taken</li>
          <li>Many suffer neck or back <strong>pain</strong> (62%)</li>
          <li>Many have <strong>sleep</strong> problems (34%)</li>
        </ul>
      </div>
    </div>

    <h2 class="section-title">Measurable improvements</h2>
    <p>Studies show successful corporate health problems can create:</p>
    <ul>
      <li><strong>26.8%</strong> reduction in absenteeism</li>
      <li><strong>$5.81</strong> savings on every dollar invested</li>
    </ul>

    <h2 class="section-title">What staff want and need?</h2>
    <div class="split">
      <div class="split__text">
        <p>The line between home and work has become more blurred. As a result, the work environment needs to provide as much as possible to offset the melting line of work and home. Otherwise staff will go somewhere that does provide the right benefits. If they are going to work 40 – 50 hours for you, this leaves very little time for them to do much else. They need &amp; want to remain fit and healthy as staff don’t want to be worked into the ground.</p>
        <p><strong>You can give them the piece that is missing. Make their lives better not worse.</strong></p>
      </div>
      <div class="image-slot slot-handshake" role="img" aria-label="Photo of two hands joining puzzle pieces that spell partnership"></div>
    </div>
  </div>
  <div class="foot-rule"></div>
</section>

<section class="page page--right">
  <header class="masthead">
    <div class="brand-name">KV Stride<span>Mentoring</span></div>
  </header>
  <div class="content">
    <h2 class="section-title">What I do</h2>
    <div class="split">
      <p class="split__text">I provide your company with an opportunity to reduce the high cost of absenteeism and presenteeism. By doing this, you get to position your business so it attracts and retains the highest quality of staff, at the same time as increasing revenue. You become more, when your staff become more.</p>
      <div class="image-slot slot-portrait" role="img" aria-label="Portrait photo of the coach outdoors by the water"></div>
    </div>

    <h2 class="section-title">Testimonials</h2>
    <div class="split">
      <div class="split__text">
        <p><strong>65%</strong> of people in LMD are now doing more exercise than they were 12 months ago.</p>
        <p class="highlight">“The energy post a lunch time work is enormous”</p>
      </div>
      <div class="partner-badge">LMD</div>
    </div>

    <h2 class="section-title">The offer:</h2>
    <p>To learn more about how I can help you stay ahead of the game I have put together an offer to LMD delegates.</p>
    <p>For the first 15 companies to contact me, I will come and assess your business and it’s suitability to meet the current demands of staff. For this to occur I will require some information on your business, which will remain confidential of course.</p>
  </div>

  <div class="image-slot slot-chart" role="img" aria-label="Illustration of a rising bar chart with an upward arrow"></div>

  <div class="offer-aside">
    <p>After assessing your situation I will come to your office and discuss my findings for you, so you can see where you are at where you need to get to. I will also outline how KV Stride Mentoring may be able to assist you.</p>
    <p style="margin-top:8px">You can also go to <span class="link">www.kvstridementoring.example/presentation.html</span> to see my original presentation to LMD.</p>
  </div>

  <footer class="footer-bar">
    <span>Kai Varden · KV Stride Mentoring</span>
    <span>www.kvstridementoring.example</span>
  </footer>
</section>

</body>
</html>
```